Beyond The Ledger Double Sided DL Flyer

We need a double sided flyer that we provide to a Real Estate agent for leeds. It should provide our basic services as well as a modern look and feel. The brochure should incorporate our Brand colors and have a graphic that centres around money and property. I have included a couple of pictures that we like (but have not yet purchased from PIXVAULT) as an indication of the type of picture we like.

WE need to also show the Beyond The Ledger brand and have our Phone / address's and email details.

Target Market(s)

Realestate clients (Property Investors)

Industry/Entity Type

Financial Planning

Requirements
Must have
• Picture on Front (maybe the logo on back)
• Please incorporate existing logo colours.

```html
<!DOCTYPE html>
<html lang="en">
<head>
<meta charset="utf-8">
<title>Beyond The Ledger – DL Flyer</title>
<link rel="stylesheet" href="https://fonts.googleapis.com/css2?family=Anton&family=Poppins:wght@500;600&family=Roboto:ital,wght@0,900;1,500&display=swap">
<style>
  :root {
    --page-bg: #e9e9ec;
    --paper: #f3f3ef;
    --brand-green: #2f9f45;
    --brand-lime: #7ac143;
    --ink: #111111;
    --white: #ffffff;
  }
  * { box-sizing: border-box; margin: 0; padding: 0; }
  html, body { width: 1200px; height: 1200px; overflow: hidden; }
  body { background: var(--page-bg); position: relative; font-family: "Poppins", sans-serif; }

  .flyer {
    position: absolute; top: 133px; width: 440px; height: 933px;
    background: var(--paper); overflow: hidden;
    box-shadow: 0 6px 18px rgba(0,0,0,.18);
  }
  .flyer--front { left: 120px; }
  .flyer--back { left: 640px; }

  /* Front */
  .brand {
    position: absolute; top: 62px; left: 0; width: 100%;
    display: flex; align-items: center; justify-content: center; gap: 12px;
  }
  .brand__dot { width: 18px; height: 18px; border-radius: 50%; background: var(--brand-lime); }
  .brand__name { font-family: "Poppins", sans-serif; font-weight: 600; font-size: 30px; color: var(--brand-green); letter-spacing: .5px; }

  .front-art { position: absolute; top: 170px; left: 0; }

  .phone-strip {
    position: absolute; top: 700px; left: 0; width: 100%; height: 78px;
    background: var(--paper); display: flex; align-items: center; justify-content: center;
  }
  .phone-strip__number { font-family: "Roboto", sans-serif; font-weight: 900; font-size: 46px; color: var(--ink); }

  .contact {
    position: absolute; top: 778px; left: 0; width: 100%; height: 155px;
    background: var(--brand-green); color: var(--white);
    font-family: "Roboto", sans-serif; font-style: italic; font-weight: 500; font-size: 18px;
    padding: 26px 0 0 70px;
  }
  .contact__row { display: flex; align-items: flex-start; gap: 8px; }
  .contact__row + .contact__row { margin-top: 16px; }
  .contact__icon { flex: 0 0 22px; margin-left: -30px; margin-top: 2px; }
  .contact__lines { line-height: 1.3; }

  /* Back */
  .back-wave { position: absolute; top: 0; left: 0; width: 100%; height: 140px;
    background: linear-gradient(180deg, #a9d66f 0%, #cfe8a6 45%, rgba(243,243,239,0) 100%); }
  .services__title {
    position: absolute; top: 160px; left: 62px;
    font-family: "Anton", sans-serif; font-size: 27px; line-height: 1.1; color: var(--ink); letter-spacing: .3px;
  }
  .services__list { position: absolute; top: 250px; left: 62px; list-style: none; }
  .service { display: flex; align-items: center; gap: 18px; height: 70px; }
  .service__icon { flex: 0 0 58px; }
  .service__label { font-weight: 500; font-size: 17px; line-height: 1.35; color: var(--ink); }
  .back-art {
    position: absolute; left: 0; bottom: 0; width: 100%; height: 290px;
    background: linear-gradient(160deg, rgba(243,243,239,0) 0%, #d8c67a 35%, #6fbf6a 60%, #2f9f6a 100%);
    clip-path: polygon(0 78%, 40% 55%, 62% 10%, 100% 0, 100% 100%, 0 100%);
  }
</style>
</head>
<body>

<section class="flyer flyer--front">
  <div class="brand">
    <span class="brand__dot"></span>
    <span class="brand__name">Beyond The Ledger</span>
  </div>

  <svg class="front-art" width="440" height="530" viewBox="0 0 440 530">
    <defs>
      <linearGradient id="photoTone" x1="0" y1="0" x2="0" y2="1">
        <stop offset="0" stop-color="#3f7f2c"/>
        <stop offset=".6" stop-color="#5f9a3a"/>
        <stop offset="1" stop-color="#a88a63"/>
      </linearGradient>
    </defs>
    <rect y="360" width="440" height="170" fill="var(--brand-green)"/>
    <path d="M20 110 Q220 -20 440 110 L440 380 Q220 500 20 380 Z" fill="#ffffff"/>
    <path role="img" aria-label="Photo of a hand watering a seedling in a jar of coins beside a model house and coin stacks"
          d="M28 114 Q220 -10 434 114 L434 374 Q220 490 28 374 Z" fill="url(#photoTone)"/>
  </svg>

  <div class="phone-strip"><span class="phone-strip__number">(02) 4300 1275</span></div>

  <div class="contact">
    <div class="contact__row">
      <svg class="contact__icon" width="22" height="16" viewBox="0 0 22 16"><rect x="1" y="1" width="20" height="14" fill="none" stroke="#fff" stroke-width="1.6"/><path d="M1 1 L11 9 L21 1" fill="none" stroke="#fff" stroke-width="1.6"/></svg>
      <span class="contact__lines">info@beyondtheledger.com.au</span>
    </div>
    <div class="contact__row">
      <svg class="contact__icon" width="22" height="24" viewBox="0 0 22 24"><path d="M11 2 a6 6 0 0 1 6 6 c0 5 -6 11 -6 11 s-6 -6 -6 -11 a6 6 0 0 1 6 -6z" fill="#fff"/><circle cx="11" cy="8" r="2.2" fill="var(--brand-green)"/><ellipse cx="11" cy="21" rx="7" ry="2" fill="none" stroke="#fff" stroke-width="1.4"/></svg>
      <span class="contact__lines">8 / 114 Harbour View Rd Seabrook NSW 2261<br>2 / 37 Marlow St Oakhaven NSW 2264</span>
    </div>
  </div>
</section>

<section class="flyer flyer--back">
  <div class="back-wave" role="img" aria-label="Soft flowing green light waves"></div>

  <h2 class="services__title">ACCOUNTANTS AND FINANCIAL<br>ADVISORS WHO SPECIALISE IN:</h2>

  <ul class="services__list">
    <li class="service">
      <svg class="service__icon" width="58" height="58" viewBox="0 0 58 58"><circle cx="29" cy="29" r="27" fill="var(--brand-green)" stroke="#bfe3a5" stroke-width="3"/><path d="M14 30 L24 21 L34 30 M17 28 V39 H31 V28" fill="none" stroke="#fff" stroke-width="2.4"/><text x="40" y="38" font-family="Poppins, sans-serif" font-size="15" font-weight="600" fill="#fff" text-anchor="middle">$</text></svg>
      <span class="service__label">Negative Gearing &amp;<br>Investment Properties</span>
    </li>
    <li class="service">
      <svg class="service__icon" width="58" height="58" viewBox="0 0 58 58"><circle cx="29" cy="29" r="27" fill="var(--brand-green)" stroke="#bfe3a5" stroke-width="3"/><rect x="17" y="30" width="6" height="10" fill="#fff"/><rect x="26" y="25" width="6" height="15" fill="#fff"/><rect x="35" y="19" width="6" height="21" fill="#fff"/><path d="M16 26 L28 18 L38 14" fill="none" stroke="#fff" stroke-width="2"/></svg>
      <span class="service__label">Property &amp; Capital<br>Gains Tax Minimisation</span>
    </li>
    <li class="service">
      <svg class="service__icon" width="58" height="58" viewBox="0 0 58 58"><circle cx="29" cy="29" r="27" fill="var(--brand-green)" stroke="#bfe3a5" stroke-width="3"/><circle cx="32" cy="21" r="7" fill="none" stroke="#fff" stroke-width="2"/><text x="32" y="25" font-family="Poppins, sans-serif" font-size="10" font-weight="600" fill="#fff" text-anchor="middle">$</text><path d="M13 38 Q20 31 28 34 L38 34 Q44 32 46 30" fill="none" stroke="#fff" stroke-width="2.4"/></svg>
      <span class="service__label">Self-Managed Superannuation<br>Funds (SMSF)</span>
    </li>
    <li class="service">
      <svg class="service__icon" width="58" height="58" viewBox="0 0 58 58"><circle cx="29" cy="29" r="27" fill="var(--brand-green)" stroke="#bfe3a5" stroke-width="3"/><path d="M15 29 L29 17 L43 29 M19 26 V41 H39 V26" fill="none" stroke="#fff" stroke-width="2.4"/><text x="29" y="38" font-family="Poppins, sans-serif" font-size="12" font-weight="600" fill="#fff" text-anchor="middle">$</text></svg>
      <span class="service__label">Small Business &amp; Personal<br>Taxation</span>
    </li>
    <li class="service">
      <svg class="service__icon" width="58" height="58" viewBox="0 0 58 58"><circle cx="29" cy="29" r="27" fill="var(--brand-green)" stroke="#bfe3a5" stroke-width="3"/><path d="M16 16 V41 H43" fill="none" stroke="#fff" stroke-width="2.2"/><rect x="20" y="31" width="4" height="8" fill="#fff"/><rect x="26" y="27" width="4" height="12" fill="#fff"/><circle cx="36" cy="24" r="5" fill="none" stroke="#fff" stroke-width="2"/><path d="M39.5 27.5 L43 31" stroke="#fff" stroke-width="2.2"/></svg>
      <span class="service__label">Investment Advice &amp; Risk<br>Insurances</span>
    </li>
  </ul>

  <div class="back-art" role="img" aria-label="Illustration of green model houses, gold coin stacks and rising green growth arrows"></div>
</section>

</body>
</html>
```